Brightmere Business Card Redesign & Logo Update

We need to update our business cards to something more modern and fresh. Brightmere can provide the current color schemes and old design examples, but welcome creativity in helping us with this redesign. PLEASE NOTE that we no longer utilize the "tree" and/or "leaf" imagery in our branding. If able would apprecaite an update on the quality of our "words only" logo in Ai. / PNG formats too.

Target Market(s)

Investors, landowners, corporate partners, contractors

Industry/Entity Type

Environmental Restoration & Conservation

Contact Information for Business Card

Logo, persons name, title, mailing address, phone and email, website url

Font styles to use
Other font styles liked:
• Merriweather

Requirements
Nice to have
• Logo, persons name, title, mailing address, phone and email, website url, but open to ideams
Should not have
• No all back backgrounds

```html
<!DOCTYPE html>
<html lang="en">
<head>
<meta charset="utf-8">
<title>Brightmere Business Card</title>
<link href="https://fonts.googleapis.com/css2?family=Open+Sans:wght@400;600;700&display=swap" rel="stylesheet">
<style>
  :root {
    --backdrop: #3c3c3c;
    --card-white: #ffffff;
    --card-back-top: #1d5a34;
    --card-back-bottom: #123d24;
    --brand-green: #1f7a3c;
    --edge-green: #2f9a52;
    --brand-orange: #e8782a;
    --text-grey: #6a6a6a;
    --divider: #9bbfa6;
    --logo-light: #e6efe8;
  }
  * { margin: 0; padding: 0; box-sizing: border-box; }
  html, body { width: 1200px; height: 801px; overflow: hidden; }
  body {
    background: var(--backdrop);
    font-family: "Open Sans", Arial, sans-serif;
    position: relative;
  }
  .card {
    position: absolute;
    top: 249px;
    width: 530px;
    height: 303px;
    border-bottom: 3px solid var(--brand-green);
  }
  .card-front { left: 50px; background: var(--card-white); }
  .card-back {
    left: 620px;
    background: linear-gradient(160deg, var(--card-back-top), var(--card-back-bottom));
    border-bottom-color: var(--edge-green);
  }

  .wordmark {
    position: absolute;
    left: 44px;
    top: 60px;
    font-weight: 700;
    font-size: 46px;
    letter-spacing: 1px;
    color: var(--brand-green);
    line-height: 1;
  }
  .person {
    position: absolute;
    left: 44px;
    top: 150px;
    text-align: right;
    width: 190px;
  }
  .person-name {
    font-weight: 700;
    font-size: 19px;
    color: var(--brand-green);
    letter-spacing: 0.5px;
  }
  .person-title {
    font-size: 14px;
    color: var(--text-grey);
  }
  .divider {
    position: absolute;
    left: 250px;
    top: 130px;
    width: 1px;
    height: 78px;
    background: var(--divider);
  }
  .contact-list {
    position: absolute;
    left: 268px;
    top: 128px;
    list-style: none;
  }
  .contact-list li {
    display: flex;
    align-items: center;
    gap: 8px;
    font-size: 14px;
    color: var(--text-grey);
    line-height: 26px;
  }
  .contact-list svg { width: 12px; height: 12px; fill: var(--brand-orange); }
  .address {
    position: absolute;
    left: 44px;
    bottom: 32px;
    font-size: 14px;
    color: var(--text-grey);
  }

  .back-wordmark {
    position: absolute;
    left: 0;
    right: 0;
    top: 118px;
    text-align: center;
    font-weight: 700;
    font-size: 54px;
    letter-spacing: 1px;
    color: var(--logo-light);
    line-height: 1.2;
  }
</style>
</head>
<body>
  <section class="card card-front">
    <div class="wordmark">BRIGHTMERE</div>
    <div class="person">
      <p class="person-name">DORIAN CASTELL</p>
      <p class="person-title">President</p>
    </div>
    <div class="divider"></div>
    <ul class="contact-list">
      <li>
        <svg viewBox="0 0 12 12" aria-hidden="true"><path d="M2.5 0.5l2 2.5-1.2 1.3c.8 1.7 2 2.9 3.6 3.7l1.2-1.2 2.5 2-1.4 2.4C4.6 10.6 1.2 7.3.3 1.8z"/></svg>
        949-555-0187
      </li>
      <li>
        <svg viewBox="0 0 12 12" aria-hidden="true"><path d="M0 2h12v1L6 7 0 3zM0 4.3l6 4 6-4V10H0z"/></svg>
        dcastell@brightmere.com
      </li>
      <li>
        <svg viewBox="0 0 12 12" aria-hidden="true"><circle cx="6" cy="6" r="6"/></svg>
        www.brightmere.com
      </li>
    </ul>
    <p class="address">3187 Harbor Crest Dr, Seacliff CA 92600</p>
  </section>

  <section class="card card-back">
    <div class="back-wordmark">BRIGHTMERE</div>
  </section>
</body>
</html>
```